Postcard Design

I need a postcard style insert designed that will be mailed out with a customer's monthly statement. This postcard will describe a new service offered to the customer by our company. The front of the postcard will have a design layout of the word definition for "Monetize" and similar to design layout used in a dictionary (i.e., enunciation, Verb, definition, and sample of how word is used). The backside of card will have brief description of service offered and contact information for my office.

It Company

```html
<!DOCTYPE html>
<html lang="en">
<head>
<meta charset="utf-8">
<title>Monetize Postcard</title>
<link href="https://fonts.googleapis.com/css2?family=Arimo:wght@400;700&display=swap" rel="stylesheet">
<style>
  :root {
    --ink: #111111;
    --paper: #ffffff;
    --front-bg: #000000;
    --back-bg: #e9e9e9;
    --back-mist: #d3d5d8;
    --money-green: #7f9a78;
    --money-dark: #3d4a3a;
    --brand-navy: #1f3350;
    --text-light: #ffffff;
    --footer-text: #333333;
  }
  * { box-sizing: border-box; margin: 0; padding: 0; }
  html, body { width: 724px; height: 1200px; overflow: hidden; background: var(--paper); }
  body { font-family: "Arimo", Arial, sans-serif; position: relative; }

  .card-front {
    position: absolute; left: 0; top: 0; width: 724px; height: 555px;
    background: var(--front-bg); color: var(--text-light); overflow: hidden;
  }
  .headword { position: absolute; left: 83px; top: 40px; font-size: 41px; font-weight: 400; letter-spacing: 0.5px; }
  .pronunciation { position: absolute; left: 198px; top: 96px; font-size: 17px; }
  .part-of-speech { position: absolute; left: 83px; top: 120px; font-size: 30px; }
  .definitions { position: absolute; left: 83px; top: 175px; width: 580px; list-style: none; font-size: 20px; line-height: 1.3; }
  .definitions li { display: flex; margin-bottom: 8px; }
  .definitions .num { width: 80px; flex: none; }
  .money-spread {
    position: absolute; left: 0; bottom: 0; width: 724px; height: 210px;
    background: linear-gradient(to bottom, var(--front-bg) 0%, var(--money-dark) 30%, var(--money-green) 70%, #a9bda2 100%);
  }

  .card-back {
    position: absolute; left: 0; top: 590px; width: 724px; height: 610px;
    background: var(--back-bg); overflow: hidden;
  }
  .digital-hand {
    position: absolute; inset: 0;
    background: radial-gradient(ellipse at 58% 30%, #f4f4f4 0%, var(--back-mist) 45%, #c9c4bd 75%, var(--back-bg) 100%);
  }
  .brand { position: absolute; left: 40px; top: 120px; display: flex; align-items: center; gap: 12px; }
  .brand-square { width: 26px; height: 26px; background: var(--brand-navy); }
  .brand-name { font-size: 26px; font-weight: 700; color: var(--brand-navy); }
  .offer { position: absolute; left: 0; top: 345px; width: 724px; text-align: center; color: var(--ink); font-weight: 700; font-size: 20px; line-height: 1.3; }
  .offer p + p { margin-top: 22px; }
  .footer-note { position: absolute; left: 0; top: 578px; width: 724px; text-align: center; font-size: 11px; color: var(--footer-text); }
  .footer-note .dash { position: absolute; left: 60px; }
</style>
</head>
<body>
  <section class="card-front">
    <h1 class="headword">mon-e-tize</h1>
    <div class="pronunciation">\ mä-nə-tīz \</div>
    <div class="part-of-speech">verb</div>
    <ol class="definitions">
      <li><span class="num">1.</span><span>Convert into or express in the form of currency.</span></li>
      <li><span class="num">2.</span><span>Convert real estate contract into currency that can be used to purchase goods and services.</span></li>
    </ol>
    <div class="money-spread" role="img" aria-label="Photo of a large spread of paper dollar bills"></div>
  </section>

  <section class="card-back">
    <div class="digital-hand" role="img" aria-label="Photo of a finger touching a glowing dollar icon among floating currency symbols"></div>
    <div class="brand"><span class="brand-square"></span><span class="brand-name">Keystone Realty</span></div>
    <div class="offer">
      <p>Interested in knowing what your real estate contract is worth if<br>you were to sell it for a lump sum cash payment?</p>
      <p>Call Ledger Lane Funding today at 208-555-0147 for<br>a free no-obligation quote on the cash value of your contract.</p>
    </div>
    <p class="footer-note"><span class="dash">-</span>Your privacy is assured. Your escrow servicing providing this opportunity to you as a confidential courtesy</p>
  </section>
</body>
</html>
```